New tech executive consulting company needs professionally branded document templates

We are a new business selling fractional board advisory and go-to-market consulting services into the Technology space. Partwise Helm are experts in providing high-quality executive-level leaders on a part-time basis to tech companies in need of their expertise. We work closely with clients to understand their business needs, challenges, and goals, and provides customised solutions to help them succeed. Due to our audience we need the design to have a high quality, executive look and feel.

Our first website is live and can be found at partwisehelm.tech. We also already have a logo which I've uploaded. Our brand is clean and uses orange to give it colour and an identity that stands out.

We need some document master templates created so we can create our own presentations (Google Slides & Powerpoint), PDF documents, and Word templates, and ideally also a LinkedIn banner.

```html
<!DOCTYPE html>
<html lang="en">
<head>
<meta charset="utf-8">
<title>Partwise Helm – Presentation Template</title>
<link href="https://fonts.googleapis.com/css2?family=Roboto:wght@700;900&family=Lato:wght@400;700&display=swap" rel="stylesheet">
<style>
  :root{
    --orange:#ee7d45;
    --navy:#272d3b;
    --navy-band:#323847;
    --peach:#fcf1ec;
    --page:#fbf3f0;
    --ink:#2a2f3b;
    --body:#5a5e66;
    --white:#ffffff;
  }
  *{margin:0;padding:0;box-sizing:border-box}
  html,body{width:1200px;height:4051px;overflow:hidden;background:var(--page)}
  body{position:relative;font-family:"Lato",sans-serif;color:var(--ink)}
  .slide{position:absolute;left:77px;width:1046px;height:588px;overflow:hidden;background:var(--white);box-shadow:0 4px 14px rgba(0,0,0,.08)}
  .slide--dark{background:var(--navy)}
  .bg{position:absolute;inset:0;width:100%;height:100%}
  .logo{position:absolute;font-family:"Roboto",sans-serif;font-weight:700;font-size:24px;letter-spacing:3px;line-height:1.05;text-align:center;color:var(--ink)}
  .slide--dark .logo{color:var(--white)}
  .logo--right{left:780px;top:30px;width:220px}
  .logo--left{left:48px;top:38px;width:220px}
  .slide-title{position:absolute;left:60px;top:50px;font-family:"Roboto",sans-serif;font-weight:700;font-size:33px;color:var(--ink)}
  .accent{color:var(--orange)}
  .rule{position:absolute;left:0;height:3px;background:var(--orange)}
  .photo{position:absolute}
  .social-dot{position:absolute;width:28px;height:28px;border-radius:50%;border:2px solid var(--white)}
  .hero-head{position:absolute;left:58px;top:252px;font-family:"Roboto",sans-serif;font-weight:700;font-size:28px;line-height:41px;color:var(--white)}
  .founder-frame{position:absolute;left:96px;top:138px;width:108px;height:108px;background:var(--orange)}
  .name{position:absolute;left:486px;top:216px;font-family:"Roboto",sans-serif;font-weight:700;font-size:26px;color:var(--ink)}
  .copy{position:absolute;font-size:12.5px;line-height:22px;color:var(--body);text-align:justify}
  .copy p+p{margin-top:14px}
  .about-head{position:absolute;left:82px;top:176px;font-family:"Roboto",sans-serif;font-weight:700;font-size:27px;line-height:37px;color:var(--ink)}
  .card{position:absolute;top:167px;width:278px;height:344px;background:var(--white);box-shadow:0 3px 14px rgba(0,0,0,.1);text-align:center}
  .card__mark{position:absolute;left:50%;top:56px;width:50px;height:50px;margin-left:-25px;transform:rotate(45deg);background:var(--orange)}
  .card__mark--dark{background:var(--navy)}
  .card__title{position:absolute;left:0;right:0;top:152px;font-size:14.5px;font-weight:700;letter-spacing:.3px;color:var(--ink)}
  .card__title--accent{color:var(--orange)}
  .card__text{position:absolute;left:18px;right:18px;top:190px;font-size:11.5px;line-height:21px;color:var(--body)}
  .features{position:absolute;left:580px;top:190px;width:465px;list-style:none}
  .features li{position:relative;padding-left:22px;padding-right:22px;font-size:11.5px;line-height:20px;color:var(--body);text-align:justify;margin-bottom:8px}
  .features li::before{content:"»";position:absolute;left:0;top:0;color:var(--orange);font-weight:700}
  .thanks{position:absolute;left:58px;top:168px;font-family:"Roboto",sans-serif;font-weight:900;font-size:50px;color:var(--white)}
  .contact{position:absolute;left:58px;top:270px;list-style:none}
  .contact li{display:flex;align-items:flex-start;color:var(--white);font-size:16px;line-height:24px;margin-bottom:20px}
  .contact svg{width:30px;height:26px;margin-right:30px;flex:none}
</style>
</head>
<body>

<!-- Cover -->
<section class="slide slide--dark" style="top:88px">
  <svg class="bg" viewBox="0 0 1046 588" preserveAspectRatio="none">
    <defs>
      <linearGradient id="coverPhoto" x1="0" y1="0" x2="1" y2="1">
        <stop offset="0" stop-color="#7d8a96"/><stop offset=".5" stop-color="#b9a89a"/><stop offset="1" stop-color="#c5cbd3"/>
      </linearGradient>
    </defs>
    <polygon points="200,0 380,0 -10,588 -190,588" fill="var(--navy-band)"/>
    <polygon points="647,0 1046,0 1046,588 253,588" fill="url(#coverPhoto)" role="img" aria-label="Photo of a smiling businesswoman in a meeting with a colleague"/>
    <line x1="645" y1="0" x2="251" y2="588" stroke="var(--orange)" stroke-width="6"/>
  </svg>
  <div class="logo logo--left">PARTWISE<br>HELM</div>
  <h1 class="hero-head">EXPERTS IN PROVIDING<br>EXECUTIVE <span class="accent">LEADERSHIP</span><br>ON DEMAND</h1>
  <div class="rule" style="left:58px;top:376px;width:132px"></div>
  <div class="social-dot" style="left:61px;top:531px"></div>
</section>

<!-- Founder -->
<section class="slide" style="top:738px">
  <svg class="bg" viewBox="0 0 1046 588" preserveAspectRatio="none">
    <polygon points="360,0 440,0 40,588 -40,588" fill="var(--peach)"/>
    <polygon points="960,0 1046,0 1046,20 660,588 580,588" fill="var(--peach)"/>
  </svg>
  <h2 class="slide-title">OUR <span class="accent">FOUNDER</span></h2>
  <div class="rule" style="top:84px;width:157px"></div>
  <div class="logo logo--right">PARTWISE<br>HELM</div>
  <div class="founder-frame"></div>
  <div class="photo" role="img" aria-label="Portrait of the founder" style="left:118px;top:160px;width:292px;height:360px;background:linear-gradient(160deg,#6b5a4a,#2d3f63 70%,#1f2a44)"></div>
  <h3 class="name"><span class="accent">TOM</span> ASHBY</h3>
  <div class="copy" style="left:486px;top:276px;width:464px">
    <p>Tom Ashby is a highly accomplished business leader with extensive experience in executive-level leadership and strategy. As the founder of Partwise Helm, Tom brings his years of experience in the technology industry to help companies achieve their goals.</p>
    <p>Throughout his career, Tom has held executive positions in companies ranging from startups to large corporations. He has a deep understanding of the tech industry and has helped companies at all stages of maturity drive significant growth and innovation.</p>
  </div>
</section>

<!-- About -->
<section class="slide" style="top:1397px">
  <svg class="bg" viewBox="0 0 1046 588" preserveAspectRatio="none">
    <polygon points="360,0 440,0 40,588 -40,588" fill="var(--peach)"/>
    <polygon points="960,0 1046,0 1046,20 660,588 580,588" fill="var(--peach)"/>
  </svg>
  <h2 class="slide-title">ABOUT <span class="accent">US</span></h2>
  <div class="rule" style="top:84px;width:157px"></div>
  <div class="logo logo--right">PARTWISE<br>HELM</div>
  <h3 class="about-head">THE SMART WAY TO<br>SCALE <span class="accent">YOUR BUSINESS</span></h3>
  <div class="copy" style="left:82px;top:272px;width:365px;font-size:11.5px;line-height:19.5px">
    <p>Partwise Helm are experts in providing high-quality executive-level leaders on a part-time basis to tech companies in need of their expertise. We work closely with clients to understand their business needs, challenges, and goals, and provides customised solutions to help them succeed.</p>
    <p>Our strategic insights, leadership, and collaborative approach make us a valuable partner for companies looking to drive growth and innovation. We are passionate about helping companies achieve their goals and are committed to providing the highest level of service to our clients.</p>
  </div>
  <div class="photo" role="img" aria-label="Photo of a team meeting in a bright office" style="left:502px;top:153px;width:462px;height:354px;background:linear-gradient(135deg,#5d6a72,#a9b3a6 45%,#3c4350)"></div>
</section>

<!-- Services -->
<section class="slide" style="top:2056px">
  <svg class="bg" viewBox="0 0 1046 588" preserveAspectRatio="none">
    <polygon points="360,0 440,0 40,588 -40,588" fill="var(--peach)"/>
    <polygon points="960,0 1046,0 1046,20 660,588 580,588" fill="var(--peach)"/>
  </svg>
  <h2 class="slide-title">OUR <span class="accent">SERVICES</span></h2>
  <div class="rule" style="top:84px;width:157px"></div>
  <div class="logo logo--right">PARTWISE<br>HELM</div>
  <article class="card" style="left:72px">
    <div class="card__mark"></div>
    <h4 class="card__title">LOREM IPSUM DOL</h4>
    <p class="card__text">Lorem ipsum dolor sit amet, consectetur adipiscing elit, sed do eiusmod tempor incididunt ut labore et dolore magna aliqua. Ut enim ad minim veniam, quis nostrud exercitation ullamco laboris nisi ut aliquip ex ea commodo consequat.</p>
  </article>
  <article class="card" style="left:384px">
    <div class="card__mark card__mark--dark"></div>
    <h4 class="card__title card__title--accent">LOREM IPSUM DOL</h4>
    <p class="card__text">Lorem ipsum dolor sit amet, consectetur adipiscing elit, sed do eiusmod tempor incididunt ut labore et dolore magna aliqua. Ut enim ad minim veniam, quis nostrud exercitation ullamco laboris nisi ut aliquip ex ea commodo consequat.</p>
  </article>
  <article class="card" style="left:695px">
    <div class="card__mark"></div>
    <h4 class="card__title">LOREM IPSUM DOL</h4>
    <p class="card__text">Lorem ipsum dolor sit amet, consectetur adipiscing elit, sed do eiusmod tempor incididunt ut labore et dolore magna aliqua. Ut enim ad minim veniam, quis nostrud exercitation ullamco laboris nisi ut aliquip ex ea commodo consequat.</p>
  </article>
</section>

<!-- Features -->
<section class="slide" style="top:2715px">
  <svg class="bg" viewBox="0 0 1046 588" preserveAspectRatio="none">
    <polygon points="360,0 440,0 40,588 -40,588" fill="var(--peach)"/>
    <polygon points="960,0 1046,0 1046,20 660,588 580,588" fill="var(--peach)"/>
  </svg>
  <h2 class="slide-title">OUR <span class="accent">FEATURES</span></h2>
  <div class="rule" style="top:84px;width:157px"></div>
  <div class="logo logo--right">PARTWISE<br>HELM</div>
  <div class="photo" role="img" aria-label="Photo of two colleagues reviewing work at a computer" style="left:80px;top:153px;width:462px;height:354px;background:linear-gradient(120deg,#e6e8ea,#b8a392 50%,#2e3447)"></div>
  <ul class="features">
    <li>Lorem ipsum dolor sit amet, consectetur adipiscing elit, sed do eiusmod tempor incididunt ut labore et dolore magna aliqua. Ut enim ad minim veniam, quis nostrud exercitation.</li>
    <li>Lorem ipsum dolor sit amet, consectetur adipiscing elit, sed do eiusmod tempor incididunt ut labore.</li>
    <li>Lorem ipsum dolor sit amet, consectetur adipiscing elit, sed do eiusmod tempor incididunt ut labore et dolore magna aliqua. Ut enim ad minim veniam, quis nostrud exercitation.</li>
    <li>Lorem ipsum dolor sit amet, consectetur adipiscing elit, sed do eiusmod tempor incididunt ut labore.</li>
    <li>Lorem ipsum dolor sit amet, consectetur adipiscing elit, sed do eiusmod tempor incididunt ut labore et dolore magna aliqua. Ut enim ad minim veniam, quis nostrud exercitation.</li>
  </ul>
</section>

<!-- Closing -->
<section class="slide slide--dark" style="top:3374px">
  <svg class="bg" viewBox="0 0 1046 588" preserveAspectRatio="none">
    <defs>
      <linearGradient id="closePhoto" x1="0" y1="0" x2="1" y2="1">
        <stop offset="0" stop-color="#3b3530"/><stop offset=".55" stop-color="#8a6a4d"/><stop offset="1" stop-color="#c9b9a6"/>
      </linearGradient>
    </defs>
    <polygon points="200,0 380,0 -10,588 -190,588" fill="var(--navy-band)"/>
    <polygon points="647,0 1046,0 1046,588 253,588" fill="url(#closePhoto)" role="img" aria-label="Photo of hands with documents beside a laptop on a wooden desk"/>
    <line x1="645" y1="0" x2="251" y2="588" stroke="var(--orange)" stroke-width="6"/>
  </svg>
  <div class="logo logo--left">PARTWISE<br>HELM</div>
  <h2 class="thanks">THANK <span class="accent">YOU</span></h2>
  <div class="rule" style="top:232px;width:228px"></div>
  <ul class="contact">
    <li><svg viewBox="0 0 30 26"><path d="M6 3l5 0 2 6-3 2c2 4 4 6 8 8l2-3 6 2 0 5c-1 2-3 2-5 2C12 24 4 15 4 6c0-2 1-3 2-3z" fill="var(--orange)"/></svg>+44 7700 900123</li>
    <li><svg viewBox="0 0 30 26"><g fill="none" stroke="var(--orange)" stroke-width="2"><circle cx="15" cy="13" r="11"/><ellipse cx="15" cy="13" rx="5" ry="11"/><line x1="4" y1="13" x2="26" y2="13"/><line x1="6" y1="7" x2="24" y2="7"/><line x1="6" y1="19" x2="24" y2="19"/></g></svg>https://partwisehelm.tech/</li>
    <li><svg viewBox="0 0 30 26"><rect x="2" y="5" width="26" height="17" fill="var(--orange)"/><path d="M2 5l13 10 13-10" fill="none" stroke="var(--navy)" stroke-width="2"/></svg>info@partwisehelm.tech</li>
    <li><svg viewBox="0 0 30 26"><path d="M15 1a8 8 0 0 1 8 8c0 6-8 13-8 13S7 15 7 9a8 8 0 0 1 8-8z" fill="var(--orange)"/><circle cx="15" cy="9" r="3" fill="var(--navy)"/><ellipse cx="15" cy="23" rx="9" ry="2" fill="none" stroke="var(--orange)" stroke-width="1.5"/></svg>Alderbury, England,<br>United Kingdom</li>
  </ul>
  <div class="social-dot" style="left:61px;top:529px"></div>
</section>

</body>
</html>
```